Velcora flyer

this flyer is to promote a new product Velcora for feminine hygiene

Target Market(s)

general population

Industry/Entity Type

Pharmacy

Requirements
Must have
• picture of velcora
• Picture of ladies in the flyer
Nice to have
• Only Available at Brindle pharmacy

```html
<!DOCTYPE html>
<html lang="en">
<head>
<meta charset="utf-8">
<title>Velcora Flyer – Brindle Pharmacy</title>
<link href="https://fonts.googleapis.com/css2?family=Roboto+Condensed:wght@400;700&family=Titillium+Web:wght@400;600&family=Open+Sans:wght@400;600&display=swap" rel="stylesheet">
<style>
  :root {
    --green: #6aab46;
    --green-bright: #7cc242;
    --purple: #3b1640;
    --grey-text: #5a5a5a;
    --dark: #222;
    --light-grey: #e6e6e6;
    --white: #ffffff;
    --skin-a: #e9cbb8;
    --skin-b: #c99a82;
    --box-a: #8a2f7e;
    --box-b: #4a1547;
    --soap-a: #cfe6ea;
    --soap-b: #86b8c2;
  }
  * { margin: 0; padding: 0; box-sizing: border-box; }
  html, body { width: 698px; height: 1200px; overflow: hidden; background: #fff; }
  .flyer {
    position: relative; width: 698px; height: 1200px; overflow: hidden;
    background: var(--white); font-family: "Open Sans", sans-serif; color: var(--grey-text);
  }
  .hero-photo {
    position: absolute; left: 0; top: 0; width: 520px; height: 480px;
    background: radial-gradient(ellipse at 30% 35%, var(--skin-a) 0%, var(--skin-b) 55%, #f4f4f4 100%);
  }
  .hero-flowers {
    position: absolute; left: 300px; top: 100px; width: 330px; height: 250px;
    background: radial-gradient(ellipse at center, #ffffff 0%, rgba(255,255,255,0.7) 45%, rgba(255,255,255,0) 70%);
  }
  .wave { position: absolute; left: 0; top: 360px; width: 698px; height: 240px; }

  .brand {
    position: absolute; right: 22px; top: 70px;
    display: flex; align-items: center; gap: 8px;
  }
  .brand-mark { width: 14px; height: 14px; background: var(--green); }
  .brand-name {
    font-family: "Roboto Condensed", sans-serif; font-weight: 700; font-size: 21px;
    line-height: 1; color: var(--purple);
  }

  .title-block { position: absolute; left: 50px; top: 448px; font-family: "Roboto Condensed", sans-serif; font-weight: 700; }
  .product-name { font-size: 66px; line-height: 1; color: var(--green); letter-spacing: 0.5px; }
  .tagline { font-size: 27px; line-height: 1.05; text-transform: uppercase; }
  .tagline .accent { color: var(--green-bright); display: block; }
  .tagline .muted { color: var(--grey-text); display: block; }

  .benefits {
    position: absolute; left: 0; top: 596px; width: 698px; height: 256px;
    background: var(--green); color: var(--white); padding: 12px 0 0 42px;
  }
  .section-title { font-family: "Titillium Web", sans-serif; font-weight: 600; font-size: 27px; line-height: 1.2; }
  .benefits .section-title { margin-bottom: 12px; }
  .bullets { list-style: none; width: 380px; }
  .bullets li { position: relative; font-size: 13px; line-height: 1.4; margin-bottom: 6px; padding-left: 30px; }
  .bullets li::before { content: ""; position: absolute; left: 0; top: 7px; width: 5px; height: 5px; border-radius: 50%; background: currentColor; }

  .product-box {
    position: absolute; left: 487px; top: 548px; width: 155px; height: 300px;
    background: linear-gradient(160deg, var(--box-a), var(--box-b));
    box-shadow: 4px 4px 10px rgba(0,0,0,0.25);
  }
  .soap-photo {
    position: absolute; left: 57px; top: 868px; width: 242px; height: 150px; border-radius: 50%;
    background: radial-gradient(ellipse at 40% 35%, var(--soap-a), var(--soap-b));
  }
  .why-not { position: absolute; left: 317px; top: 862px; width: 370px; color: var(--green); }
  .why-not .section-title { margin-bottom: 8px; }
  .why-not .bullets { width: 370px; }
  .why-not .bullets li { font-size: 12.5px; padding-left: 24px; margin-bottom: 6px; color: #333; }
  .why-not .bullets li::before { background: var(--green); }

  .how-to { position: absolute; left: 0; top: 1058px; width: 350px; height: 124px; }
  .how-to svg { position: absolute; inset: 0; width: 100%; height: 100%; }
  .how-to-content { position: relative; padding: 10px 0 0 42px; }
  .how-to .section-title { color: var(--green); margin-bottom: 6px; }
  .how-to .bullets { width: 280px; }
  .how-to .bullets li { font-size: 11.5px; line-height: 1.35; padding-left: 26px; margin-bottom: 5px; color: #333; }
  .how-to .bullets li::before { background: var(--green); top: 6px; }

  .contact-call { position: absolute; left: 361px; top: 1106px; color: var(--dark); }
  .contact-call .label { font-size: 18px; line-height: 1.2; }
  .contact-call .phone { font-size: 20px; font-weight: 600; line-height: 1.2; }
  .contact-divider { position: absolute; left: 510px; top: 1098px; width: 1px; height: 68px; background: #bbb; }
  .contact-links { position: absolute; left: 530px; top: 1112px; list-style: none; font-size: 12px; color: #333; }
  .contact-links li { display: flex; align-items: center; gap: 8px; margin-bottom: 6px; }
  .contact-links svg { width: 12px; height: 12px; }

  .footer-bar { position: absolute; left: 0; bottom: 0; width: 698px; height: 12px; background: linear-gradient(90deg, var(--green) 0 568px, var(--light-grey) 568px); }
</style>
</head>
<body>
<main class="flyer">
  <div class="hero-photo" role="img" aria-label="Photo of a young woman's neck and shoulder with soft skin tones"></div>
  <div class="hero-flowers" role="img" aria-label="White orchid sprig resting on the shoulder"></div>

  <svg class="wave" viewBox="0 0 698 240" preserveAspectRatio="none" aria-hidden="true">
    <path d="M0 80 C 160 10, 320 0, 420 60 C 520 120, 620 150, 698 120 L698 240 L0 240 Z" fill="#ffffff"/>
    <path d="M0 80 C 160 10, 320 0, 420 60 C 520 120, 620 150, 698 100 L698 112 C 620 165, 520 135, 420 78 C 320 20, 160 30, 0 98 Z" fill="#6aab46"/>
    <path d="M0 98 C 160 30, 320 20, 420 78 C 520 135, 620 165, 698 112 L698 118 C 620 172, 520 142, 420 86 C 320 30, 160 40, 0 106 Z" fill="#3b1640"/>
  </svg>

  <div class="brand">
    <span class="brand-mark"></span>
    <span class="brand-name">Brindle Pharmacy</span>
  </div>

  <header class="title-block">
    <h1 class="product-name">VELCORA</h1>
    <p class="tagline"><span class="accent">For the young and</span><span class="muted">confident girl in you</span></p>
  </header>

  <section class="benefits">
    <h2 class="section-title">Why use Velcora?</h2>
    <ul class="bullets">
      <li>Use Velcora for complete hygiene and cleansing of the intimate region.</li>
      <li>Helps relieve symptoms like itching, irritation, burning dryness and keeps unwanted odour away.</li>
      <li>Restores and maintains natural intimate pH balance.</li>
      <li>Provides long-lasting freshness, promoting a healthy and hygienic lifestyle.</li>
      <li>Keeps you clean fresh and makes you feel confident.</li>
    </ul>
  </section>

  <div class="product-box" role="img" aria-label="Velcora intimate wash bottle and carton in purple packaging"></div>

  <div class="soap-photo" role="img" aria-label="Bar of pale blue soap with foam"></div>

  <section class="why-not">
    <h2 class="section-title">Why not use soap?</h2>
    <ul class="bullets">
      <li>Soaps can be very harsh on the sensitive skin of the intimate area as they are alkaline based.</li>
      <li>It may cause an imbalance of the normal growth of healthy bacteria and lead to possible infections.</li>
      <li>The chemicals present in soap may cause dryness in the perineal area, leading to discomfort.</li>
      <li>Soaps have a pH balance &gt; 8, which leads to disturbance in the natural pH balance in the intimate area.</li>
    </ul>
  </section>

  <section class="how-to">
    <svg viewBox="0 0 350 124" preserveAspectRatio="none" aria-hidden="true">
      <polygon points="0,0 328,0 350,124 0,124" fill="#6aab46"/>
      <polygon points="14,4 324,4 344,120 14,120" fill="#e6e6e6"/>
    </svg>
    <div class="how-to-content">
      <h2 class="section-title">How To Use Velcora</h2>
      <ul class="bullets">
        <li>Gently squeeze the bottle to take a few drops of Velcora.</li>
        <li>Apply to the inmate area &amp; rinse with water.</li>
      </ul>
    </div>
  </section>

  <div class="contact-call">
    <p class="label">Call Us</p>
    <p class="phone">1234 567 789</p>
  </div>
  <div class="contact-divider"></div>
  <ul class="contact-links">
    <li><svg viewBox="0 0 12 12"><circle cx="6" cy="6" r="5" fill="none" stroke="#333" stroke-width="1.2"/><path d="M1 6h10M6 1c-2 3-2 7 0 10M6 1c2 3 2 7 0 10" fill="none" stroke="#333" stroke-width="0.8"/></svg>www.website.com</li>
    <li><svg viewBox="0 0 12 12"><circle cx="6" cy="6" r="5" fill="none" stroke="#333" stroke-width="1.2"/><circle cx="6" cy="6" r="2" fill="#333"/></svg>info@website.com</li>
  </ul>

  <div class="footer-bar"></div>
</main>
</body>
</html>
```